Business cards for law firm with global theme

I'd like business cards with contact info for two offices. They should include the colors and font of the new logo design, which is a stylized globe with an "F" in it. The feel should be very modern and professional.

```html
<!DOCTYPE html>
<html lang="en">
<head>
<meta charset="utf-8">
<title>Veranti Law – Business Cards</title>
<link href="https://fonts.googleapis.com/css2?family=Montserrat:wght@400;500;600;700&display=swap" rel="stylesheet">
<style>
  :root {
    --stage: #2a2a2c;
    --navy: #063f74;
    --navy-deep: #053461;
    --cyan: #0fa9e6;
    --sky: #1b7fd1;
    --white: #ffffff;
  }
  * { box-sizing: border-box; margin: 0; padding: 0; }
  html, body { width: 1200px; height: 881px; overflow: hidden; }
  body {
    background: var(--stage);
    font-family: "Montserrat", Arial, sans-serif;
    display: flex;
    align-items: center;
    justify-content: center;
    gap: 40px;
  }
  .card {
    position: relative;
    width: 540px;
    height: 309px;
    border-radius: 14px;
    overflow: hidden;
  }
  /* Back of card */
  .card-back {
    background: var(--navy);
    display: flex;
    align-items: center;
    justify-content: center;
  }
  .brand {
    display: flex;
    align-items: center;
    gap: 16px;
  }
  .brand-dot {
    border-radius: 50%;
  }
  .brand-name {
    font-weight: 700;
    line-height: 1;
    letter-spacing: 1px;
    text-align: right;
  }
  .brand-name span { display: block; }
  .brand-name .sub { font-size: 0.45em; letter-spacing: 3px; margin-top: 4px; }
  .card-back .brand-dot { width: 64px; height: 64px; background: var(--navy-deep); }
  .card-back .brand-name { font-size: 40px; color: var(--sky); }

  /* Front of card */
  .card-front { background: var(--white); }
  .front-bands { position: absolute; inset: 0; }
  .card-front .brand {
    position: absolute;
    top: 34px;
    right: 36px;
  }
  .card-front .brand-dot { width: 54px; height: 54px; background: var(--cyan); }
  .card-front .brand-name { font-size: 32px; color: var(--navy); }

  .person {
    position: absolute;
    left: 36px;
    top: 186px;
    color: var(--white);
  }
  .person-name {
    color: var(--cyan);
    font-weight: 700;
    font-size: 19px;
    letter-spacing: 1.5px;
    text-transform: uppercase;
  }
  .person-role { font-size: 13px; margin: 2px 0 8px; }
  .contact-list { list-style: none; font-size: 12.5px; }
  .contact-list li { display: flex; align-items: center; gap: 8px; line-height: 1.45; }
  .contact-list svg { width: 11px; height: 11px; flex: none; }

  .address {
    position: absolute;
    right: 34px;
    top: 200px;
    color: var(--white);
    font-size: 12.5px;
    line-height: 1.5;
    text-align: right;
  }
</style>
</head>
<body>

  <section class="card card-back" aria-label="Card back">
    <div class="brand">
      <span class="brand-dot"></span>
      <div class="brand-name"><span>VERANTI</span><span class="sub">LAW</span></div>
    </div>
  </section>

  <section class="card card-front" aria-label="Card front">
    <svg class="front-bands" viewBox="0 0 540 309" preserveAspectRatio="none" aria-hidden="true">
      <path d="M0,146 Q300,166 540,48 L540,309 L0,309 Z" fill="var(--cyan)"/>
      <path d="M0,148 Q300,170 540,62 L540,309 L0,309 Z" fill="var(--white)"/>
      <path d="M0,152 Q300,176 540,70 L540,309 L0,309 Z" fill="var(--navy)"/>
    </svg>

    <div class="brand">
      <span class="brand-dot"></span>
      <div class="brand-name"><span>VERANTI</span><span class="sub">LAW</span></div>
    </div>

    <div class="person">
      <p class="person-name">Daniel Carver</p>
      <p class="person-role">Director</p>
      <ul class="contact-list">
        <li>
          <svg viewBox="0 0 12 12"><path d="M3 1 L4.8 3.4 L3.8 4.6 Q5 7 7.4 8.2 L8.6 7.2 L11 9 L9.6 11 Q4 10.6 1 3 Z" fill="var(--cyan)"/></svg>
          201 555-0142
        </li>
        <li>
          <svg viewBox="0 0 12 12"><rect x="1" y="2.5" width="10" height="7" fill="none" stroke="var(--cyan)" stroke-width="1.2"/><path d="M1 2.5 L6 6.5 L11 2.5" fill="none" stroke="var(--cyan)" stroke-width="1.2"/></svg>
          info@verantilaw.com
        </li>
        <li>
          <svg viewBox="0 0 12 12"><circle cx="6" cy="6" r="5" fill="none" stroke="var(--cyan)" stroke-width="1.1"/><ellipse cx="6" cy="6" rx="2.2" ry="5" fill="none" stroke="var(--cyan)" stroke-width="1"/><path d="M1 6 H11" stroke="var(--cyan)" stroke-width="1"/></svg>
          www.verantilaw.com
        </li>
      </ul>
    </div>

    <p class="address">480 Harlow St.<br>Ste. 212, NYC, NY 10014</p>
  </section>

</body>
</html>
```